Mobile phone signal boosting solutions needs a website

We need a website design for the reselling of a mobile signal boosting product set. These solutions are Vexlor exempt and will provide an indoor signal for mobile phones. We would like to see designs that incorporate the colours and feel of our logo. The domain will be
openmeadow.com / co.uk
Overview of the company and how it is to be used: Open meadow (domain name) will work with business and end user to provide mobile signal boosting – where people struggle indoors with a mobile signal our solutions will help by finding the smallest signal and boosting it, allowing users to use voice and data over their mobile network (please note this is not wireless signal boosting)
Number of Pages:
-Home
-Solutions / How it works
-Case Studies
-Contact
Text content: Currently just use placeholders
Technical specs : Wordpress and ability to use CMS if that’s relevant
Target Market(s)
Business professional all markets /high end residential
Coded - Design and coding required
4 page

```html
<!DOCTYPE html>
<html lang="en">
<head>
<meta charset="utf-8">
<title>Open meadow – Mobile Signal Boosters</title>
<link rel="stylesheet" href="https://fonts.googleapis.com/css2?family=Comfortaa:wght@400;600;700&family=Montserrat:wght@600;700;800&family=Questrial&display=swap">
<style>
:root{
  --yellow:#ffd400;
  --gold:#f4b400;
  --ink:#111111;
  --text:#333333;
  --muted:#777777;
  --grey-band:#d5d5d5;
  --cream:#fff6cf;
  --line:#dcdcdc;
  --white:#ffffff;
}
*{box-sizing:border-box;margin:0;padding:0}
html,body{width:1200px;height:4376px;overflow:hidden}
body{position:relative;background:var(--white);font-family:"Questrial",sans-serif;color:var(--text)}
section,header,footer{position:absolute;left:0;width:1200px}
.abs{position:absolute}
.heading{font-family:"Comfortaa",sans-serif;font-weight:400;font-size:34px;color:var(--gold);text-align:center;position:absolute;left:0;width:1200px}
.lede{position:absolute;left:0;width:1200px;text-align:center;font-size:12.5px;color:var(--text)}
.btn-outline{position:absolute;display:flex;align-items:center;justify-content:center;gap:14px;border:2px solid var(--ink);font-family:"Montserrat",sans-serif;font-weight:600;font-size:12px;color:var(--ink);background:transparent}
.chev{width:7px;height:7px;border-right:2px solid currentColor;border-top:2px solid currentColor;transform:rotate(45deg)}
.arrow-nav{position:absolute;width:16px;height:16px;border-left:3px solid var(--ink);border-bottom:3px solid var(--ink)}
.arrow-nav.left{transform:rotate(45deg)}
.arrow-nav.right{transform:rotate(-135deg)}

/* header */
.site-header{top:0;height:82px;background:var(--white)}
.brand{position:absolute;left:122px;top:26px;display:flex;align-items:center;gap:8px;font-family:"Questrial",sans-serif;font-size:20px;color:var(--ink)}
.brand-mark{width:12px;height:12px;background:var(--gold)}
.main-nav{position:absolute;left:444px;top:34px;display:flex;gap:34px;font-family:"Montserrat",sans-serif;font-weight:600;font-size:12px;color:var(--ink)}
.main-nav .active{color:var(--gold)}
.search{position:absolute;left:872px;top:27px;width:206px;height:34px;background:#eeeeee;font-size:11px;color:#aaa;padding:10px 8px}
.search svg{position:absolute;right:10px;top:9px}

/* hero */
.hero{top:82px;height:586px;background:linear-gradient(180deg,#8f9aa8 0%,#b9a89a 45%,#e3a45a 78%,#f08a1c 100%)}
.hero-title{position:absolute;left:119px;top:135px;font-family:"Montserrat",sans-serif;font-weight:800;font-size:36px;line-height:50px;color:var(--white)}
.hero-copy{position:absolute;left:119px;top:290px;width:470px;font-size:14px;line-height:19px;color:var(--white)}
.hero .btn-outline{left:117px;top:375px;width:144px;height:43px;border:1px solid var(--white);color:var(--white);font-size:11px;font-weight:600}

/* products */
.products{top:668px;height:476px}
.product-row{position:absolute;left:226px;top:132px;width:746px;height:220px;border:1px solid var(--line);display:flex}
.product{flex:1;border-right:1px solid var(--line);text-align:center}
.product:last-child{border-right:0}
.product-img{margin:14px auto 0;width:164px;height:124px}
.product-name{margin-top:20px;font-size:12.5px;color:var(--ink)}
.product-more{margin-top:18px;font-size:9px;color:var(--gold)}

/* about */
.about{top:1144px;height:410px;background:var(--grey-band)}
.about-card{position:absolute;left:184px;top:56px;width:409px;height:298px;background:var(--white)}
.about-card h2{position:absolute;left:29px;top:36px;font-family:"Comfortaa",sans-serif;font-weight:400;font-size:33px;color:var(--gold)}
.about-card p{position:absolute;left:29px;top:90px;width:340px;font-size:12.5px;line-height:19px}
.about-card .btn-outline{left:28px;top:208px;width:142px;height:42px}
.about-photos{position:absolute;left:593px;top:56px;width:424px;height:298px;display:grid;grid-template-columns:240px 90px 90px;grid-template-rows:84px 92px 118px;gap:3px}
.about-photos div{background:linear-gradient(135deg,#6f6253,#c2a27a)}

/* why */
.why{top:1554px;height:591px}
.why-grid{position:absolute;left:121px;top:143px;width:957px;height:399px;border:1px solid var(--line);display:flex}
.why-item{position:relative;border-right:1px solid var(--line);padding:0 25px}
.why-item:last-child{border-right:0}
.why-icon{position:absolute;top:44px;right:12px;width:64px;height:64px;border-radius:50%;background:var(--yellow);display:flex;align-items:center;justify-content:center}
.why-item h3{position:absolute;top:138px;left:25px;font-family:"Comfortaa",sans-serif;font-weight:600;font-size:21px;line-height:26px;color:var(--gold)}
.why-item .rule{position:absolute;top:214px;left:25px;width:52px;height:1px;background:var(--gold)}
.why-item p{position:absolute;top:238px;left:25px;right:20px;font-size:12.5px;line-height:17.5px}

/* solution */
.solution{top:2145px;height:527px;background:var(--cream)}
.solution .heading{color:var(--ink);top:42px}
.sol-card{position:absolute;top:150px;height:250px;background:var(--white)}
.sol-img{height:167px;background:linear-gradient(180deg,#fbf6ee,#f3eadc)}
.sol-name{position:absolute;left:12px;bottom:33px;font-size:12.5px;color:var(--ink)}
.sol-go{position:absolute;right:14px;bottom:32px;width:16px;height:16px;border:1px solid var(--ink);border-radius:50%}
.sol-go::after{content:"";position:absolute;left:4px;top:4.5px;width:4px;height:4px;border-right:1.3px solid var(--ink);border-top:1.3px solid var(--ink);transform:rotate(45deg)}

/* where */
.where{top:2672px;height:516px}
.where-strip{position:absolute;left:121px;top:130px;width:957px;height:328px;display:flex;gap:3px}
.where-main{width:301px;position:relative;background:linear-gradient(180deg,#7fb3e6 0%,#b7c6d1 40%,#7b5c52 75%,#5b5060 100%)}
.where-main span{position:absolute;left:0;right:0;bottom:0;height:38px;background:rgba(240,200,0,.82);font-family:"Comfortaa",sans-serif;font-weight:700;font-size:19px;color:var(--ink);text-align:center;line-height:40px}
.where-panel{flex:1;position:relative;background:linear-gradient(180deg,#e6c21a,#cfa80e)}
.where-panel span{position:absolute;top:40px;left:50%;writing-mode:vertical-rl;transform:translateX(-50%);font-family:"Comfortaa",sans-serif;font-weight:700;font-size:19px;color:var(--ink);white-space:nowrap}

/* note */
.note{top:3188px;height:503px;background:linear-gradient(135deg,#dcdcdc,#cfcfcf)}
.note h2{position:absolute;left:121px;top:50px;font-family:"Comfortaa",sans-serif;font-weight:400;font-size:34px;color:var(--ink)}
.field{position:absolute;left:121px;width:316px;background:var(--white);font-size:11px;color:#999;padding:12px 18px}
.submit{position:absolute;left:121px;top:414px;width:114px;height:39px;background:var(--yellow);font-family:"Montserrat",sans-serif;font-weight:700;font-size:12px;color:var(--ink);display:flex;align-items:center;justify-content:center}

/* cta */
.cta{top:3691px;height:294px;background:var(--yellow)}
.cta-visual{position:absolute;left:208px;top:56px;width:168px;height:170px;border-radius:6px;background:linear-gradient(135deg,#2a2a2a,#111111)}
.cta h2{position:absolute;left:396px;top:88px;font-family:"Montserrat",sans-serif;font-weight:800;font-size:33px;line-height:42px;color:var(--ink)}
.cta .btn-outline{left:529px;top:192px;width:143px;height:42px;font-size:11px}

/* footer */
.site-footer{top:3985px;height:391px;background:var(--ink);color:var(--white)}
.site-footer .brand{left:122px;top:86px;color:var(--white);font-size:22px}
.foot-about{position:absolute;left:122px;top:162px;width:260px;font-size:12px;line-height:19.5px}
.foot-divider{position:absolute;top:68px;width:1px;height:258px;background:#555}
.foot-title{position:absolute;top:74px;font-family:"Montserrat",sans-serif;font-weight:600;font-size:18px}
.foot-links{position:absolute;left:476px;top:125px;list-style:none;font-family:"Montserrat",sans-serif;font-weight:600;font-size:12px}
.foot-links li{height:39px}
.social{position:absolute;left:476px;top:286px;display:flex;gap:19px}
.social span{width:25px;height:25px;background:var(--yellow)}
.contact-row{position:absolute;left:760px;display:flex;gap:20px;font-size:12.5px;line-height:17px}
.copyright{position:absolute;left:0;top:367px;width:1200px;height:24px;background:var(--yellow);color:var(--ink);font-size:12px;text-align:center;line-height:24px}
</style>
</head>
<body>

<header class="site-header">
  <div class="brand"><span class="brand-mark"></span>Open meadow</div>
  <nav class="main-nav">
    <span class="active">HOME</span><span>SOLUTIONS</span><span>CASE STUDIES</span><span>CONTACT</span>
  </nav>
  <div class="search">Search Here
    <svg width="16" height="16" viewBox="0 0 16 16"><circle cx="6.5" cy="6.5" r="5" fill="none" stroke="#222" stroke-width="1.6"/><line x1="10.2" y1="10.2" x2="14.5" y2="14.5" stroke="#222" stroke-width="1.8"/></svg>
  </div>
</header>

<section class="hero" role="img" aria-label="Photograph of cell towers silhouetted against a sunset sky">
  <h1 class="hero-title">THE FIRST CELL SIGNAL<br>BOOSTER FOR OVERLANDING &amp;<br>OFF-ROADING</h1>
  <p class="hero-copy">Meet the first cell signal booster designed for overlanders by overlanders. The TrailLink Reach Rover is the ultimate booster for peace of mind in remote areas.</p>
  <div class="btn-outline">LEARN MORE <span class="chev"></span></div>
</section>

<section class="products">
  <h2 class="heading" style="top:50px">Customize The Products You Need</h2>
  <p class="lede" style="top:98px">We have been a professional manufacturer and solution provider of an indoor signal for mobile phones.</p>
  <span class="arrow-nav left" style="left:124px;top:234px"></span>
  <div class="product-row">
    <div class="product"><div class="product-img" role="img" aria-label="Illustration of GNSS signal coverage" style="background:linear-gradient(135deg,#2c67c9,#8fc3f0)"></div><div class="product-name">GNSS Signal coverage</div><div class="product-more">Details ⟶</div></div>
    <div class="product"><div class="product-img" role="img" aria-label="Illustration of mobile communication" style="background:linear-gradient(135deg,#f2f4fa,#cfd9ee)"></div><div class="product-name">Mobile Communication</div><div class="product-more">Details ⟶</div></div>
    <div class="product"><div class="product-img" role="img" aria-label="Illustration of critical communication network" style="background:linear-gradient(135deg,#2fb6c9,#e2633b)"></div><div class="product-name">Critical Communication</div><div class="product-more">Details ⟶</div></div>
    <div class="product"><div class="product-img" role="img" aria-label="Illustration of jamming signal scenario" style="background:linear-gradient(135deg,#39b7e6,#bfe8f6)"></div><div class="product-name">Jmming Signal</div><div class="product-more">Details ⟶</div></div>
  </div>
  <span class="arrow-nav right" style="left:1058px;top:234px"></span>
  <div class="btn-outline" style="left:529px;top:389px;width:143px;height:43px">LEARN MORE <span class="chev"></span></div>
</section>

<section class="about">
  <div class="about-card">
    <h2>About Us</h2>
    <p>Lorem ipsum dolor sit amet, consectetur adipiscing elit, sed do eiusmod tempor incididunt ut labore et dolore magna aliqua. Quis ipsum suspendisse ultrices gravida. Risus commodo viverra maecenas accumsan lacus vel facilisis.</p>
    <div class="btn-outline">LEARN MORE <span class="chev"></span></div>
  </div>
  <div class="about-photos" role="img" aria-label="Collage of office team, telecom towers, a router, an engineer and a support agent">
    <div style="grid-row:1/3"></div>
    <div style="background:linear-gradient(135deg,#5f87b8,#a8c2da)"></div>
    <div style="background:linear-gradient(135deg,#1b7fa8,#3aa9d1)"></div>
    <div style="grid-column:2/4;grid-row:2/4;background:linear-gradient(135deg,#dcdcdc,#7a2e2a)"></div>
    <div style="background:linear-gradient(135deg,#6aa0d8,#d9a64a)"></div>
  </div>
</section>

<section class="why">
  <h2 class="heading" style="top:46px">Why Choose Us</h2>
  <p class="lede" style="top:95px">Lorem ipsum dolor sit amet, consectetur adipiscing elit, sed do eiusmod tempor incididunt ut labore et</p>
  <div class="why-grid">
    <div class="why-item" style="width:234px">
      <div class="why-icon"><svg width="30" height="30" viewBox="0 0 30 30" fill="none" stroke="#fff" stroke-width="2"><path d="M15 3 L26 9 L26 21 L15 27 L4 21 L4 9 Z M4 9 L15 15 L26 9 M15 15 L15 27"/></svg></div>
      <h3>Product<br>Service</h3><span class="rule"></span>
      <p>Fieldwave provides wide range of products &amp; services for turnkey projects, such as repeater, BDA, jammer, BTS/IBS passive components and antenna.</p>
    </div>
    <div class="why-item" style="width:243px">
      <div class="why-icon"><svg width="30" height="30" viewBox="0 0 30 30" fill="none" stroke="#fff" stroke-width="2"><circle cx="15" cy="15" r="5"/><circle cx="15" cy="15" r="10" stroke-dasharray="4 3"/></svg></div>
      <h3>Customized<br>Solution</h3><span class="rule"></span>
      <p>With a team of well-trained engineers and responsive service chain standby, Fieldwave timely understands customers' needs and provide proper solution accordingly.</p>
    </div>
    <div class="why-item" style="width:240px">
      <div class="why-icon"><svg width="30" height="30" viewBox="0 0 30 30" fill="none" stroke="#fff" stroke-width="2"><rect x="7" y="5" width="16" height="21"/><line x1="10" y1="11" x2="20" y2="11"/><line x1="10" y1="16" x2="20" y2="16"/><line x1="10" y1="21" x2="17" y2="21"/></svg></div>
      <h3>Customized<br>Product</h3><span class="rule"></span>
      <p>Being a veteran on manufacturing highly customized products, Fieldwave excels in tailor-made products required by customers upon diverse circumstances.</p>
    </div>
    <div class="why-item" style="flex:1">
      <div class="why-icon"><svg width="30" height="30" viewBox="0 0 30 30" fill="none" stroke="#fff" stroke-width="2"><path d="M6 17 V14 A9 9 0 0 1 24 14 V17"/><rect x="4" y="16" width="5" height="7" rx="1"/><rect x="21" y="16" width="5" height="7" rx="1"/><path d="M24 23 Q22 27 16 27"/></svg></div>
      <h3>Technical<br>Support</h3><span class="rule"></span>
      <p>Equipped with complete sets of tools for testing, installation and maintenance, Fieldwave is capable of delivering remote or field technical support whenever necessary.</p>
    </div>
  </div>
</section>

<section class="solution">
  <h2 class="heading">Solution</h2>
  <p class="lede" style="top:106px">We provide the infrastructure and total solutions to mobile operators and enterprises to enhance the trunked radio/cellular network.</p>
  <span class="arrow-nav left" style="left:72px;top:266px"></span>
  <div class="sol-card" style="left:124px;width:291px"><div class="sol-img" role="img" aria-label="Diagram of a macro RF ICS repeater setup"></div><div class="sol-name">Macro RF ICS Repeater Solution</div><span class="sol-go"></span></div>
  <div class="sol-card" style="left:449px;width:291px"><div class="sol-img" role="img" aria-label="Diagram of a frequency shift repeater setup"></div><div class="sol-name">Frequency Shift Repeater Solution</div><span class="sol-go"></span></div>
  <div class="sol-card" style="left:775px;width:303px"><div class="sol-img" role="img" aria-label="Diagram of a fiber optic repeater setup"></div><div class="sol-name">Fiber Optic Repeater Solution</div><span class="sol-go"></span></div>
  <span class="arrow-nav right" style="left:1108px;top:266px"></span>
  <div class="btn-outline" style="left:529px;top:431px;width:143px;height:43px">LEARN MORE <span class="chev"></span></div>
</section>

<section class="where">
  <h2 class="heading" style="top:58px">Where is The Product Used</h2>
  <div class="where-strip">
    <div class="where-main" role="img" aria-label="Photograph of a container ship at a port"><span>Transportation</span></div>
    <div class="where-panel" role="img" aria-label="Aviation scene with yellow tint"><span>Aviation</span></div>
    <div class="where-panel" role="img" aria-label="Commercial building with yellow tint"><span style="top:52px">Commercial &amp; Industry</span></div>
    <div class="where-panel" role="img" aria-label="Railway train with yellow tint"><span style="top:125px">Railway</span></div>
    <div class="where-panel" role="img" aria-label="Government building with yellow tint"><span style="top:105px">Government</span></div>
    <div class="where-panel" role="img" aria-label="Navigation device with yellow tint"><span style="top:110px">Navigation</span></div>
  </div>
</section>

<section class="note" role="img" aria-label="Faint world map background">
  <h2>Send Us A Note</h2>
  <div class="field" style="top:124px;height:39px">Name</div>
  <div class="field" style="top:171px;height:39px">Email</div>
  <div class="field" style="top:217px;height:39px">Country</div>
  <div class="field" style="top:263px;height:116px">Message</div>
  <div class="submit">SUBMIT</div>
</section>

<section class="cta">
  <div class="cta-visual" role="img" aria-label="Illustration of a magnifying glass with a question mark"></div>
  <h2>Do you have questions or comments?<br>We can help!</h2>
  <div class="btn-outline">CONTACT US</div>
</section>

<footer class="site-footer">
  <div class="brand"><span class="brand-mark"></span>Open meadow</div>
  <p class="foot-about">Lorem ipsum dolor sit amet, consectetur adipiscing elit, sed do eiusmod tempor incididunt ut labore et dolore magna aliqua. Quis ipsum suspendisse ultrices gravida. Risus commodo viverra maecenas</p>
  <span class="foot-divider" style="left:456px"></span>
  <span class="foot-divider" style="left:740px"></span>
  <div class="foot-title" style="left:476px">QUICK LINKS</div>
  <ul class="foot-links"><li>HOME</li><li>SOLUTIONS</li><li>CASE STUDIES</li><li>CONTACT</li></ul>
  <div class="social"><span></span><span></span><span></span><span></span></div>
  <div class="foot-title" style="left:758px">CONTACT US</div>
  <div class="contact-row" style="top:126px">
    <svg width="34" height="34" viewBox="0 0 34 34"><circle cx="17" cy="17" r="16" fill="none" stroke="#ffd400" stroke-width="1.5"/><rect x="9" y="11" width="16" height="12" fill="#ffd400"/><path d="M9 11 L17 18 L25 11" fill="none" stroke="#111" stroke-width="1.5"/></svg>
    <div><div style="font-size:12px">Email</div><div style="color:var(--yellow);font-size:17px;margin-top:2px">info@openmeadow.net</div></div>
  </div>
  <div class="contact-row" style="top:182px;left:768px">
    <svg width="14" height="14" viewBox="0 0 14 14"><path d="M3 1 L6 4 L4 6 Q6 9 8 10 L10 8 L13 11 L11 13 Q5 13 1 3 Z" fill="#ffd400"/></svg>
    <span>+00-000-55018</span>
  </div>
  <div class="contact-row" style="top:214px;left:768px">
    <svg width="14" height="18" viewBox="0 0 14 18"><path d="M7 1 A6 6 0 0 1 13 7 Q13 11 7 17 Q1 11 1 7 A6 6 0 0 1 7 1 Z" fill="#ffd400"/><circle cx="7" cy="7" r="2.2" fill="#111"/></svg>
    <span>Lorem ipsum dolor sit amet,<br>consectetur adipiscing elit.<br>Nullam felis ligula,</span>
  </div>
  <div class="copyright">Copyright © 2023 Open meadow Co.,Ltd. All rights reserved.</div>
</footer>

</body>
</html>
```